business card for mobile ultrasound business
Coastline Portable Scans
business card for mobile ultrasound business - Medical
Creative Brief
Professional
Theodore R. Dalby
Senior Executive
738 Heron Bluff Lane Myrtle Beach, SC 29461
coastlineportablescans@mailbox-example.net

```html
<!DOCTYPE html>
<html lang="en">
<head>
<meta charset="utf-8">
<title>Coastline Portable Scans – Business Card</title>
<link rel="stylesheet" href="https://fonts.googleapis.com/css2?family=Open+Sans:wght@400;600;700&display=swap">
<style>
  :root {
    --page-bg: #e4e6e8;
    --card-bg: #ffffff;
    --ink-dark: #3a3f44;
    --ink-brand: #0f5a88;
    --blue-deep: #0a4f7c;
    --blue-mid: #1f86bd;
    --blue-light: #4cb1de;
    --blue-pale: #7cc8ea;
    --text-on-blue: #ffffff;
  }
  * { box-sizing: border-box; margin: 0; padding: 0; }
  html, body {
    width: 1200px; height: 883px; overflow: hidden;
    background: var(--page-bg);
    font-family: "Open Sans", Arial, sans-serif;
  }
  .sheet {
    width: 1200px; height: 883px;
    display: flex; align-items: center; justify-content: center; gap: 40px;
  }
  .card {
    position: relative;
    width: 540px; height: 310px;
    background: var(--card-bg);
    border-radius: 22px;
    box-shadow: 0 6px 18px rgba(0,0,0,0.12);
    overflow: hidden;
  }

  /* Front */
  .brand {
    position: absolute; left: 60px; top: 104px; width: 240px;
    display: flex; flex-direction: column; align-items: center; gap: 8px;
  }
  .brand-dot {
    width: 18px; height: 18px; border-radius: 50%;
    background: var(--ink-brand);
  }
  .brand-name {
    font-size: 22px; font-weight: 700; color: var(--ink-brand);
    line-height: 1.15; letter-spacing: 0.5px; text-transform: uppercase;
    text-align: center;
  }
  .web-band {
    position: absolute; left: 330px; right: 0; top: 112px; height: 58px;
    background: linear-gradient(90deg, var(--blue-mid), var(--blue-light));
    display: flex; align-items: center; padding-left: 14px;
  }
  .web-band span {
    color: var(--text-on-blue); font-size: 9px; letter-spacing: 0.3px;
    text-transform: uppercase; white-space: nowrap;
  }

  /* Back */
  .identity {
    position: absolute; left: 150px; top: 40px;
    text-transform: uppercase; color: var(--ink-dark);
  }
  .identity .name { font-size: 22px; font-weight: 400; letter-spacing: 0.5px; }
  .identity .name strong { font-weight: 700; color: var(--blue-deep); }
  .identity .title { font-size: 10px; font-weight: 600; letter-spacing: 0.6px; margin-top: 2px; }

  .contact-band {
    position: absolute; left: 0; right: 0; top: 100px; height: 120px;
    display: flex;
  }
  .contact-phone {
    width: 46%;
    background: linear-gradient(90deg, var(--blue-deep), var(--blue-mid));
    color: var(--text-on-blue);
    display: flex; flex-direction: column; justify-content: flex-end;
    align-items: flex-end; padding: 0 22px 18px 0;
    font-size: 11px; line-height: 1.35; text-transform: uppercase;
  }
  .contact-online {
    flex: 1;
    background: linear-gradient(90deg, var(--blue-light), var(--blue-pale));
    color: var(--text-on-blue);
    padding: 14px 0 0 20px;
    font-size: 10px; line-height: 1.45; text-transform: uppercase;
  }
  .contact-online .online-value { text-transform: lowercase; white-space: nowrap; }
  .label { font-weight: 600; }
  .address {
    position: absolute; left: 248px; top: 238px;
    font-size: 9.5px; color: var(--ink-dark); line-height: 1.45;
    text-transform: uppercase; letter-spacing: 0.3px;
  }
  .address strong { font-weight: 700; }
</style>
</head>
<body>
<main class="sheet">
  <section class="card card-front" aria-label="Card front">
    <div class="brand">
      <span class="brand-dot"></span>
      <span class="brand-name">Coastline<br>Portable Scans</span>
    </div>
    <div class="web-band"><span>www.coastlinescans-example.com</span></div>
  </section>

  <section class="card card-back" aria-label="Card back">
    <div class="identity">
      <p class="name">Theodore R. <strong>Dalby</strong></p>
      <p class="title">Senior Executive</p>
    </div>
    <div class="contact-band">
      <div class="contact-phone">
        <span class="label">Phone &amp; Fax</span>
        <span>+1 843 555 0142</span>
        <span>+1 843 555 0187</span>
      </div>
      <div class="contact-online">
        <p class="label">Email &amp; Web</p>
        <p class="online-value">coastlineportablescans@mailbox-example.net</p>
        <p class="online-value">www.coastlinescans-example.com</p>
      </div>
    </div>
    <p class="address">738 Heron Bluff Lane, <strong>Myrtle Beach</strong><br><strong>SC 29461</strong></p>
  </section>
</main>
</body>
</html>
```